Powder detergent

We need a design for packaging of powder detergent. Packaging is plastic 3 kg. Brand of product is VORU. Current sub-brand is Glintrax 4. We suggest to change sub-brand using 'Lumina white', 'Lumina clean', 'Lumina color', whatever but keeping unchanged words VORU and Lumina.
Herewith attached you may find pictures of current designs we have.
If you need more info please let me know.
Updates

Target Market(s)

women 25-65 years old, in Albanian market

Industry/Entity Type

Plastic

Requirements
Must have
• Brand VORU must be unchanged in color and font.
The word 'Lumina' must be as sub-brand, free to be changed in color and font.

```html
<!DOCTYPE html>
<html lang="sq">
<head>
<meta charset="utf-8">
<title>VORU – powder detergent pack front</title>
<link rel="stylesheet" href="https://fonts.googleapis.com/css2?family=Archivo+Black&display=swap">
<style>
  :root {
    --pack-white: #ffffff;
    --mist-grey: #eef0f2;
    --leaf-green: #8fcf2a;
    --leaf-light: #d9f0a8;
    --aqua: #5fc8ec;
    --aqua-light: #c9ecf8;
    --deep-blue: #2f5fd8;
    --sub-brand-blue: #1d3f9e;
    --brand-red: #c8001c;
    --shirt-white: #f4f5f6;
    --shirt-shade: #dfe2e5;
  }
  html, body {
    margin: 0;
    padding: 0;
    overflow: hidden;
    background: var(--pack-white);
  }
  .pack-front {
    position: relative;
    width: 899px;
    height: 1200px;
    overflow: hidden;
    background: var(--pack-white);
  }
  .artwork {
    position: absolute;
    inset: 0;
    width: 899px;
    height: 1200px;
  }
  .brand-lockup {
    position: absolute;
    left: 0;
    top: 380px;
    width: 899px;
    margin: 0;
    text-align: center;
    font-family: "Archivo Black", "Arial Black", sans-serif;
    font-weight: 400;
    font-size: 240px;
    line-height: 1;
    letter-spacing: 6px;
    color: var(--brand-red);
  }
  .sub-brand {
    position: absolute;
    left: 0;
    top: 650px;
    width: 899px;
    margin: 0;
    text-align: center;
    font-family: "Archivo Black", "Arial Black", sans-serif;
    font-weight: 400;
    font-size: 60px;
    line-height: 1;
    letter-spacing: 2px;
    color: var(--sub-brand-blue);
  }
</style>
</head>
<body>
<main class="pack-front">
  <svg class="artwork" viewBox="0 0 899 1200" xmlns="http://www.w3.org/2000/svg">
    <defs>
      <radialGradient id="green-swirl-tone" cx="0.35" cy="0.35" r="0.7">
        <stop offset="0" stop-color="var(--leaf-light)"/>
        <stop offset="0.55" stop-color="var(--leaf-green)"/>
        <stop offset="1" stop-color="var(--pack-white)" stop-opacity="0"/>
      </radialGradient>
      <radialGradient id="aqua-swirl-tone" cx="0.5" cy="0.5" r="0.55">
        <stop offset="0" stop-color="var(--pack-white)"/>
        <stop offset="0.55" stop-color="var(--aqua-light)"/>
        <stop offset="0.85" stop-color="var(--aqua)"/>
        <stop offset="1" stop-color="var(--pack-white)" stop-opacity="0"/>
      </radialGradient>
      <linearGradient id="blue-flow-tone" x1="0" y1="0" x2="1" y2="1">
        <stop offset="0" stop-color="var(--deep-blue)" stop-opacity="0.85"/>
        <stop offset="0.5" stop-color="var(--aqua)"/>
        <stop offset="1" stop-color="var(--aqua-light)"/>
      </linearGradient>
      <linearGradient id="mesh-tone" x1="0" y1="0" x2="0" y2="1">
        <stop offset="0" stop-color="var(--pack-white)"/>
        <stop offset="1" stop-color="var(--mist-grey)"/>
      </linearGradient>
      <linearGradient id="shirt-tone" x1="0" y1="0" x2="1" y2="1">
        <stop offset="0" stop-color="var(--shirt-white)"/>
        <stop offset="1" stop-color="var(--shirt-shade)"/>
      </linearGradient>
    </defs>

    <g role="img" aria-label="Soft grey honeycomb texture on the lower left">
      <rect x="0" y="760" width="560" height="440" fill="url(#mesh-tone)"/>
    </g>

    <g role="img" aria-label="Flowing green leaf-like swirl at the top left">
      <ellipse cx="230" cy="200" rx="290" ry="240" fill="url(#green-swirl-tone)"/>
    </g>

    <g role="img" aria-label="Flowing blue water swirl sweeping to the lower right">
      <path d="M330 1200 C420 980 600 820 899 700 L899 1200 Z" fill="url(#blue-flow-tone)" opacity="0.75"/>
      <path d="M140 690 C330 760 620 760 820 640 C700 780 420 830 140 690 Z" fill="var(--deep-blue)" opacity="0.55"/>
    </g>

    <g role="img" aria-label="Translucent aqua water ring behind the brand name">
      <ellipse cx="460" cy="540" rx="420" ry="270" fill="url(#aqua-swirl-tone)" transform="rotate(-10 460 540)"/>
    </g>

    <g role="img" aria-label="Illustration of clean white polo shirt and dress shirt">
      <rect x="560" y="820" width="320" height="380" rx="30" fill="url(#shirt-tone)"/>
    </g>
  </svg>

  <h1 class="brand-lockup">VORU</h1>
  <p class="sub-brand">Lumina white</p>
</main>
</body>
</html>
```